PPT Template for an investment fund to use in their pitchbooks

Our firm is an international investment fund and are seeking a PPT template to use in our pitch book (and subsequent PPTs). We would need a template for a title slide and then subsequent text/info slides. A clean & uncluttered feel is preferred as well as no watermark on slides. Please see our logo attached. The logo color code is #19478d. Font is Gotham-Medium.

Target Market(s)

Sophisticated investors

Industry/Entity Type

Finance

Colors
ffffff
0356a4

```html
<!DOCTYPE html>
<html lang="en">
<head>
<meta charset="utf-8">
<title>Corvane Capital Partners – Master Slide Presentation</title>
<link href="https://fonts.googleapis.com/css2?family=Montserrat:wght@500;600;700&family=Open+Sans:wght@400;600&display=swap" rel="stylesheet">
<style>
:root{
  --blue:#1c4a9b;
  --blue-deep:#19478d;
  --blue-soft:#e7ecf5;
  --track:#dde2ea;
  --ink:#333b48;
  --muted:#8a8f98;
  --page:#e9e9e9;
  --white:#ffffff;
  --grey-panel:#f1f1f1;
}
*{margin:0;padding:0;box-sizing:border-box}
html,body{width:1200px;height:3759px;overflow:hidden;background:var(--page)}
body{position:relative;font-family:"Open Sans",Arial,sans-serif;color:var(--ink)}
.slide{position:absolute;width:562px;height:317px;background:var(--white);overflow:hidden;box-shadow:0 2px 6px rgba(0,0,0,.12)}
.left{left:23px}.right{left:607px}
.slide.blue{background:var(--blue)}
.slide.grey{background:var(--grey-panel)}
.abs{position:absolute}
.heading{position:absolute;left:40px;top:30px;font-family:"Montserrat",sans-serif;font-weight:600;font-size:20px;color:var(--blue)}
.title{font-family:"Montserrat",sans-serif;font-weight:600;color:var(--blue);font-size:19px}
.body{font-size:6.3px;line-height:1.5;color:var(--muted);text-align:justify}
.center{text-align:center}
.pnum{position:absolute;right:38px;bottom:24px;font-size:5px;color:var(--blue);font-weight:600}
.btn{position:absolute;height:13px;padding:0 11px;border-radius:7px;background:var(--blue);color:#fff;font-family:"Montserrat",sans-serif;font-weight:600;font-size:5.5px;line-height:13px;letter-spacing:.2px;box-shadow:0 0 0 2px var(--blue-soft)}
.plus{position:absolute;width:17px;height:17px;border-radius:50%;background:var(--blue);color:#fff;font-size:10px;line-height:17px;text-align:center;font-family:"Montserrat",sans-serif;box-shadow:0 0 0 2px #fff}
.photo{position:absolute}
.round{border-radius:9px}
.city{background:linear-gradient(180deg,#f2c2a8 0%,#c89aa6 45%,#5b4660 100%)}
.cloud{background:linear-gradient(180deg,#cfe0ee 0%,#eef3f8 55%,#d8e1ea 100%)}
.arch{background:linear-gradient(135deg,#f4f4f4 0%,#b9b9b9 60%,#777 100%)}
.office{background:linear-gradient(160deg,#cfd9e6 0%,#6d86a8 50%,#2f3e57 100%)}
.desk{background:linear-gradient(135deg,#f2f2f2 0%,#c4c4c4 55%,#3a3a3a 100%)}
.tower{background:linear-gradient(200deg,#d0d0d0 0%,#8a8a8a 40%,#2a2a2a 100%)}
.avatar{border-radius:50%;background:radial-gradient(circle at 50% 40%,#c9c9c9,#6f6f6f)}
.brand{font-family:"Montserrat",sans-serif;font-weight:600;font-size:10px;letter-spacing:.3px}
.brand .dot{display:inline-block;width:9px;height:9px;border-radius:50%;background:currentColor;margin-right:5px;vertical-align:-1px}
.bigtitle{position:absolute;left:40px;top:180px;padding-left:12px;border-left:2px solid currentColor;font-family:"Montserrat",sans-serif;font-weight:600;font-size:22px;line-height:1.1}
.url{position:absolute;left:28px;top:282px;font-size:4.6px;letter-spacing:1.6px;font-weight:600}
.card{position:absolute;background:#fff;border-radius:8px;box-shadow:0 2px 7px rgba(0,0,0,.12)}
.label{font-family:"Montserrat",sans-serif;font-weight:600;font-size:7px;color:var(--blue)}
.dark{color:var(--ink)}
.bullets{list-style:none;font-size:5.2px;color:var(--muted);line-height:2}
.bullets li::before{content:"";display:inline-block;width:4px;height:4px;border-radius:50%;background:var(--blue);margin-right:4px}
.tick{position:absolute;width:18px;height:18px}
.bar-track{position:absolute;height:4px;background:var(--track);border-radius:2px}
.bar-fill{position:absolute;left:0;top:0;height:4px;background:var(--blue);border-radius:2px}
.big-num{font-family:"Montserrat",sans-serif;font-weight:500;font-size:28px;color:var(--ink)}
.vdivider{position:absolute;top:100px;width:1px;height:150px;background:#e5e5e5}
</style>
</head>
<body>

<!-- Row 1 -->
<section class="slide left" style="top:28px">
  <div class="abs brand" style="left:30px;top:80px;color:var(--blue)"><span class="dot"></span>CORVANE CAPITAL</div>
  <div class="bigtitle" style="color:var(--blue)">MASTER SLIDE<br>PRESENTATION</div>
  <div class="url" style="color:var(--blue)">WWW.CORVANECAPITAL.COM</div>
  <div class="photo" role="img" aria-label="Blue architectural cover image" style="left:330px;top:0;width:232px;height:317px;background:linear-gradient(160deg,#3d68b3,#1c4a9b)"></div>
</section>

<section class="slide right blue" style="top:28px">
  <div class="abs brand" style="left:30px;top:80px;color:#fff"><span class="dot"></span>CORVANE CAPITAL</div>
  <div class="bigtitle" style="color:#fff">MASTER SLIDE<br>PRESENTATION</div>
  <div class="url" style="color:#fff">WWW.CORVANECAPITAL.COM</div>
  <div class="photo arch" role="img" aria-label="Bright white modern architecture photo" style="left:330px;top:0;width:232px;height:317px"></div>
</section>

<!-- Row 2 -->
<section class="slide left" style="top:365px">
  <h2 class="heading">Project Page</h2>
  <div class="photo city round" role="img" aria-label="City skyline at dusk" style="left:70px;top:88px;width:118px;height:143px"></div>
  <div class="photo cloud round" role="img" aria-label="Tower above the clouds" style="left:219px;top:88px;width:118px;height:143px"></div>
  <div class="photo arch round" role="img" aria-label="White arched corridor" style="left:371px;top:88px;width:118px;height:143px"></div>
  <div class="plus" style="left:62px;top:106px">+</div>
  <div class="plus" style="left:211px;top:106px">+</div>
  <div class="plus" style="left:363px;top:106px">+</div>
  <div class="abs label" style="left:70px;top:244px;width:118px;font-size:6px"><span style="letter-spacing:1px">••••••••</span><span style="float:right">Project 01</span></div>
  <div class="abs label" style="left:219px;top:244px;width:118px;font-size:6px"><span style="letter-spacing:1px">••••••••</span><span style="float:right">Project 02</span></div>
  <div class="abs label" style="left:371px;top:244px;width:118px;font-size:6px"><span style="letter-spacing:1px">••••••••</span><span style="float:right">Project 03</span></div>
  <div class="pnum">3</div>
</section>

<section class="slide right" style="top:365px">
  <div class="abs" style="left:10px;top:50px;width:250px;height:210px;background:radial-gradient(circle at 40% 55%,#eef1f7 0%,#fff 70%)"></div>
  <div class="abs card" style="left:47px;top:112px;width:96px;height:96px;border-radius:50%;box-shadow:0 3px 12px rgba(0,0,0,.12)"></div>
  <div class="abs label" style="left:47px;top:155px;width:96px;text-align:center;font-size:9px">FUNDING</div>
  <div class="photo avatar" role="img" aria-label="Team member portrait" style="left:158px;top:18px;width:50px;height:50px;border:3px solid #fff"></div>
  <div class="photo avatar" role="img" aria-label="Team member portrait" style="left:180px;top:178px;width:50px;height:50px;border:3px solid #fff"></div>
  <div class="photo avatar" role="img" aria-label="Team member portrait" style="left:62px;top:236px;width:26px;height:26px;border:2px solid #fff"></div>
  <h3 class="abs title" style="left:292px;top:110px">Add Title Here</h3>
  <p class="abs body" style="left:292px;top:140px;width:220px">Lorem ipsum dolor sit amet, consectetur adipiscing elit, sed do eiusmod tempor incididunt ut labore et dolore magna aliqua. Ut enim ad minim veniam, quis nostrud exercitation ullamco laboris nisi ut aliquip ex ea commodo consequat. Duis aute irure dolor in reprehenderit in voluptate velit esse cillum dolore eu fugiat nulla pariatur. Excepteur sint occaecat cupidatat non proident, sunt in culpa qui officia deserunt mollit anim id est laborum perspiciatis unde.</p>
  <div class="pnum">4</div>
</section>

<!-- Row 3 -->
<section class="slide left" style="top:702px">
  <h2 class="heading">Pricing Tables</h2>
  <div class="card" style="left:44px;top:80px;width:114px;height:154px"></div>
  <div class="card" style="left:209px;top:80px;width:114px;height:154px"></div>
  <div class="card" style="left:374px;top:80px;width:114px;height:154px"></div>
  <div class="abs" style="left:44px;top:96px;width:114px;text-align:center"><div class="label dark" style="font-size:6px">Project 01</div><div class="label" style="font-size:13px;margin-top:5px">$200.00</div></div>
  <div class="abs" style="left:209px;top:96px;width:114px;text-align:center"><div class="label dark" style="font-size:6px">Project 02</div><div class="label" style="font-size:13px;margin-top:5px">$599.00</div></div>
  <div class="abs" style="left:374px;top:96px;width:114px;text-align:center"><div class="label dark" style="font-size:6px">Project 03</div><div class="label" style="font-size:13px;margin-top:5px">$930.00</div></div>
  <ul class="abs bullets" style="left:60px;top:150px"><li>Lorem ipsum dolor sit</li><li>Amet, consectetur adipiscing</li><li>Elit, sed do eiusmod tempor</li><li>Incididunt ut labore ipsum</li></ul>
  <ul class="abs bullets" style="left:225px;top:150px"><li>Lorem ipsum dolor sit</li><li>Amet, consectetur adipiscing</li><li>Elit, sed do eiusmod tempor</li><li>Incididunt ut labore ipsum</li></ul>
  <ul class="abs bullets" style="left:390px;top:150px"><li>Lorem ipsum dolor sit</li><li>Amet, consectetur adipiscing</li><li>Elit, sed do eiusmod tempor</li><li>Incididunt ut labore ipsum</li></ul>
  <div class="btn" style="left:78px;top:215px">MORE INFO</div>
  <div class="btn" style="left:243px;top:215px">MORE INFO</div>
  <div class="btn" style="left:406px;top:215px">MORE INFO</div>
  <div class="pnum">5</div>
</section>

<section class="slide right" style="top:702px">
  <svg class="abs" style="left:44px;top:112px" width="22" height="10" viewBox="0 0 22 10"><path d="M0 5H20M15 1L20 5L15 9" fill="none" stroke="#b7bfcc" stroke-width="1.2"/></svg>
  <h3 class="abs title" style="left:77px;top:104px">Section Title</h3>
  <p class="abs body" style="left:77px;top:132px;width:210px">Lorem ipsum dolor sit amet, consectetur adipiscing elit, sed do eiusmod tempor incididunt ut labore et dolore magna aliqua. Ut enim ad minim veniam, quis nostrud exercitation ullamco laboris nisi ut aliquip ex ea commodo consequat. Duis aute irure dolor in.</p>
  <div class="btn" style="left:77px;top:190px">MORE INFO</div>
  <div class="abs" style="left:400px;top:148px;font-family:Montserrat,sans-serif;font-weight:600;font-size:44px;color:var(--blue)">01</div>
</section>

<!-- Row 4 -->
<section class="slide left" style="top:1039px">
  <h2 class="heading">Infographic Page</h2>
  <svg class="abs" style="left:0;top:150px" width="562" height="167" viewBox="0 0 562 167">
    <defs><linearGradient id="area" x1="0" y1="0" x2="0" y2="1"><stop offset="0" stop-color="#1c4a9b"/><stop offset="1" stop-color="#c9d5ea"/></linearGradient></defs>
    <path d="M0 158 L80 138 L130 108 L200 80 L276 25 L330 60 L400 88 L460 102 L562 85 L562 167 L0 167Z" fill="url(#area)"/>
    <g stroke="#fff" stroke-opacity=".5" stroke-width="1"><line x1="80" y1="138" x2="80" y2="167"/><line x1="200" y1="80" x2="200" y2="167"/><line x1="276" y1="25" x2="276" y2="167"/><line x1="400" y1="88" x2="400" y2="167"/><line x1="460" y1="102" x2="460" y2="167"/></g>
  </svg>
  <div class="card" style="left:66px;top:133px;width:96px;height:108px"></div>
  <div class="abs label dark" style="left:100px;top:145px;font-size:6px">Project 01</div>
  <div class="abs label" style="left:82px;top:160px;font-size:14px;font-weight:500">• 50.10%</div>
  <p class="abs body" style="left:80px;top:206px;width:74px">Lorem ipsum dolor sit incididunt ut labore et dolore magna aliqua.</p>
  <div class="card" style="left:262px;top:186px;width:100px;height:70px"></div>
  <div class="abs label dark" style="left:294px;top:197px;font-size:6px">Project 02</div>
  <div class="abs label" style="left:280px;top:213px;font-size:14px;font-weight:500">• 20.20%</div>
  <p class="abs body" style="left:356px;top:115px;width:140px">Lorem ipsum dolor sit amet, consectetur adipiscing elit, sed do eiusmod tempor exercitation ullamco laboris nisi ut aliquip ea commodo consequat. Duis aute irure</p>
</section>

<section class="slide right" style="top:1039px">
  <h2 class="heading">Bullet List Page</h2>
  <svg class="tick" style="left:42px;top:98px" viewBox="0 0 18 18"><circle cx="9" cy="9" r="8" fill="none" stroke="#1c4a9b"/><path d="M5.5 9.2l2.3 2.3 4.6-4.8" fill="none" stroke="#1c4a9b" stroke-width="1.2"/></svg>
  <svg class="tick" style="left:290px;top:98px" viewBox="0 0 18 18"><circle cx="9" cy="9" r="8" fill="none" stroke="#1c4a9b"/><path d="M5.5 9.2l2.3 2.3 4.6-4.8" fill="none" stroke="#1c4a9b" stroke-width="1.2"/></svg>
  <svg class="tick" style="left:42px;top:180px" viewBox="0 0 18 18"><circle cx="9" cy="9" r="8" fill="none" stroke="#1c4a9b"/><path d="M5.5 9.2l2.3 2.3 4.6-4.8" fill="none" stroke="#1c4a9b" stroke-width="1.2"/></svg>
  <svg class="tick" style="left:290px;top:180px" viewBox="0 0 18 18"><circle cx="9" cy="9" r="8" fill="none" stroke="#1c4a9b"/><path d="M5.5 9.2l2.3 2.3 4.6-4.8" fill="none" stroke="#1c4a9b" stroke-width="1.2"/></svg>
  <div class="abs" style="left:76px;top:100px;width:190px"><div class="label" style="font-size:8px">Title text Bullet list</div><p class="body" style="margin-top:6px">Lorem ipsum dolor sit amet, consectetur adipiscing elit, sed do eiusmod tempor incididunt ut labore et dolore magna aliqua. Ut enim ad minim veniam, quis nostrud reprehenderit in voluptate velit esse cillum dolore eu et</p></div>
  <div class="abs" style="left:324px;top:100px;width:190px"><div class="label" style="font-size:8px">Title text Bullet list</div><p class="body" style="margin-top:6px">Lorem ipsum dolor sit amet, consectetur adipiscing elit, sed do eiusmod tempor incididunt ut labore et dolore magna aliqua. Ut enim ad minim veniam, quis nostrud reprehenderit in voluptate velit esse cillum dolore eu et</p></div>
  <div class="abs" style="left:76px;top:182px;width:190px"><div class="label" style="font-size:8px">Title text Bullet list</div><p class="body" style="margin-top:6px">Lorem ipsum dolor sit amet, consectetur adipiscing elit, sed do eiusmod tempor incididunt ut labore et dolore magna aliqua. Ut enim ad minim veniam, quis nostrud reprehenderit in voluptate velit esse cillum dolore eu et</p></div>
  <div class="abs" style="left:324px;top:182px;width:190px"><div class="label" style="font-size:8px">Title text Bullet list</div><p class="body" style="margin-top:6px">Lorem ipsum dolor sit amet, consectetur adipiscing elit, sed do eiusmod tempor incididunt ut labore et dolore magna aliqua. Ut enim ad minim veniam, quis nostrud reprehenderit in voluptate velit esse cillum dolore eu et</p></div>
  <div class="pnum">8</div>
</section>

<!-- Row 5 -->
<section class="slide left" style="top:1376px">
  <h2 class="heading">Number List Page</h2>
  <div class="abs center" style="left:44px;top:102px;width:120px"><div class="big-num" style="color:var(--blue);font-size:22px;font-weight:600">01</div><div class="label dark" style="color:var(--blue);margin-top:10px">Number List</div><p class="body center" style="margin-top:8px">Lorem ipsum dolor sit amet, consectetur adipiscing elit, sed do eiusmod tempor incididunt ut labore et dolore magna aliqua. Ut enim ad</p></div>
  <div class="abs center" style="left:209px;top:102px;width:120px"><div class="big-num" style="color:var(--blue);font-size:22px;font-weight:600">02</div><div class="label dark" style="color:var(--blue);margin-top:10px">Number List</div><p class="body center" style="margin-top:8px">Lorem ipsum dolor sit amet, consectetur adipiscing elit, sed do eiusmod tempor incididunt ut labore et dolore magna aliqua. Ut enim ad</p></div>
  <div class="abs center" style="left:374px;top:102px;width:120px"><div class="big-num" style="color:var(--blue);font-size:22px;font-weight:600">03</div><div class="label dark" style="color:var(--blue);margin-top:10px">Number List</div><p class="body center" style="margin-top:8px">Lorem ipsum dolor sit amet, consectetur adipiscing elit, sed do eiusmod tempor incididunt ut labore et dolore magna aliqua. Ut enim ad</p></div>
  <div class="btn" style="left:78px;top:238px">MORE INFO</div>
  <div class="btn" style="left:243px;top:238px">MORE INFO</div>
  <div class="btn" style="left:406px;top:238px">MORE INFO</div>
  <div class="pnum">9</div>
</section>

<section class="slide right" style="top:1376px">
  <div class="photo office round" role="img" aria-label="Businessman presenting at a desk" style="left:58px;top:72px;width:202px;height:175px"></div>
  <div class="plus" style="left:48px;top:84px">+</div>
  <h3 class="abs title" style="left:310px;top:100px">Title Text Here</h3>
  <p class="abs body" style="left:310px;top:130px;width:204px">Lorem ipsum dolor sit amet, consectetur adipiscing elit, sed do eiusmod tempor incididunt ut labore et dolore magna aliqua. Ut enim ad minim veniam, quis nostrud exercitation ullamco laboris nisi ut aliquip ex ea commodo consequat. Duis aute irure dolor in reprehenderit in voluptate velit esse cillum dolore eu fugiat nulla pariatur. Excepteur sint occaecat cupidatat non proident, sunt in culpa qui officia deserunt mollit anim id est laborum. Accusantium doloremque laudantium, totam rem aperiam, eaque ipsa quae ab illo inventore veritatis.</p>
  <div class="pnum">10</div>
</section>

<!-- Row 6 -->
<section class="slide left" style="top:1713px">
  <h3 class="abs title" style="left:56px;top:96px">Title Text Here</h3>
  <p class="abs body" style="left:56px;top:125px;width:186px">Lorem ipsum dolor sit amet, consectetur adipiscing elit, sed do eiusmod tempor incididunt ut labore et dolore magna aliqua. Ut enim ad minim veniam, quis nostrud reprehenderit in voluptate velit esse cillum dolore eu fugiat nulla pariatur. Excepteur sint occaecat anim id est laborum. Accusantium doloremque laudantium, totam rem aperiam, eaque ipsa quae ab illo inventore veritatis.</p>
  <div class="btn" style="left:56px;top:213px">MORE INFO</div>
  <div class="photo desk" role="img" aria-label="Hands typing on a laptop at a white desk" style="left:280px;top:0;width:282px;height:317px"></div>
  <div class="abs brand" style="left:484px;top:290px;color:#fff;font-size:5px"><span class="dot" style="width:5px;height:5px;margin-right:3px"></span>CORVANE CAPITAL</div>
</section>

<section class="slide right" style="top:1713px">
  <h2 class="heading">Funding Page</h2>
  <div class="photo city round" role="img" aria-label="City skyline at dusk" style="left:62px;top:82px;width:120px;height:88px"></div>
  <div class="photo cloud round" role="img" aria-label="Tower above the clouds" style="left:216px;top:82px;width:120px;height:88px"></div>
  <div class="photo arch round" role="img" aria-label="White arched corridor" style="left:368px;top:82px;width:120px;height:88px"></div>
  <div class="plus" style="left:154px;top:162px">+</div>
  <div class="plus" style="left:308px;top:162px">+</div>
  <div class="plus" style="left:460px;top:162px">+</div>
  <div class="abs center" style="left:62px;top:190px;width:120px"><div class="label" style="font-size:6px">Funding 01</div><p class="body center" style="margin-top:20px">Lorem ipsum dolor sit amet, consectetur adipiscing elit, sed do eiusmod tempor incididunt ut labore et dolore magna aliqua.</p></div>
  <div class="abs center" style="left:216px;top:190px;width:120px"><div class="label" style="font-size:6px">Funding 02</div><p class="body center" style="margin-top:20px">Lorem ipsum dolor sit amet, consectetur adipiscing elit, sed do eiusmod tempor incididunt ut labore et dolore magna aliqua.</p></div>
  <div class="abs center" style="left:368px;top:190px;width:120px"><div class="label" style="font-size:6px">Funding 03</div><p class="body center" style="margin-top:20px">Lorem ipsum dolor sit amet, consectetur adipiscing elit, sed do eiusmod tempor incididunt ut labore et dolore magna aliqua.</p></div>
  <div class="pnum">12</div>
</section>

<!-- Row 7 -->
<section class="slide left" style="top:2050px">
  <h2 class="heading">Countdown Page</h2>
  <div class="vdivider" style="left:200px"></div>
  <div class="vdivider" style="left:362px"></div>
  <div class="abs center" style="left:44px;top:92px;width:124px"><div class="big-num">14.5</div><div class="label" style="font-size:6px;margin-top:12px">Project Value<br>01</div><p class="body center" style="margin-top:10px">Lorem ipsum dolor sit amet, consectetur adipiscing elit, sed do eiusmod tempor incididunt ut labore et dolore magna aliqua.</p></div>
  <div class="abs center" style="left:219px;top:92px;width:124px"><div class="big-num">67.0</div><div class="label" style="font-size:6px;margin-top:12px">Project Value<br>02</div><p class="body center" style="margin-top:10px">Lorem ipsum dolor sit amet, consectetur adipiscing elit, sed do eiusmod tempor incididunt ut labore et dolore magna aliqua.</p></div>
  <div class="abs center" style="left:382px;top:92px;width:124px"><div class="big-num">85.1</div><div class="label" style="font-size:6px;margin-top:12px">Project Value<br>03</div><p class="body center" style="margin-top:10px">Lorem ipsum dolor sit amet, consectetur adipiscing elit, sed do eiusmod tempor incididunt ut labore et dolore magna aliqua.</p></div>
  <div class="btn" style="left:86px;top:236px">MORE INFO</div>
  <div class="btn" style="left:247px;top:236px">MORE INFO</div>
  <div class="btn" style="left:408px;top:236px">MORE INFO</div>
  <div class="pnum">13</div>
</section>

<section class="slide right" style="top:2050px">
  <h3 class="abs title" style="left:58px;top:100px">Title Text Here</h3>
  <p class="abs body" style="left:58px;top:128px;width:184px">Lorem ipsum dolor sit amet, consectetur adipiscing elit, sed do eiusmod tempor incididunt ut labore et dolore magna aliqua. Ut enim ad minim veniam, quis nostrud reprehenderit in voluptate velit esse cillum dolore eu fugiat nulla pariatur. Excepteur sint occaecat anim id est laborum. Accusantium doloremque laudantium, totam rem aperiam, eaque ipsa.</p>
  <div class="abs label" style="left:290px;top:106px;width:220px;font-size:5.5px">Project 01<span style="float:right;color:var(--muted)">32%</span></div>
  <div class="bar-track" style="left:290px;top:120px;width:220px"><div class="bar-fill" style="width:32%"></div></div>
  <div class="abs label" style="left:290px;top:142px;width:220px;font-size:5.5px">Project 02<span style="float:right;color:var(--muted)">61%</span></div>
  <div class="bar-track" style="left:290px;top:156px;width:220px"><div class="bar-fill" style="width:61%"></div></div>
  <div class="abs label" style="left:290px;top:178px;width:220px;font-size:5.5px">Project 03<span style="float:right;color:var(--muted)">55%</span></div>
  <div class="bar-track" style="left:290px;top:192px;width:220px"><div class="bar-fill" style="width:55%"></div></div>
  <div class="pnum">14</div>
</section>

<!-- Row 8 -->
<section class="slide left" style="top:2387px">
  <h3 class="abs title" style="left:58px;top:104px">Pie Chart</h3>
  <p class="abs body" style="left:58px;top:132px;width:184px">Lorem ipsum dolor sit amet, consectetur adipiscing elit, sed do eiusmod tempor incididunt ut labore et dolore magna aliqua. Ut enim ad minim veniam, quis nostrud reprehenderit in voluptate velit esse cillum dolore eu fugiat nulla pariatur. Excepteur sint occaecat anim id est laborum. Accusantium doloremque laudantium, totam rem aperiam, eaque.</p>
  <svg class="abs" style="left:316px;top:60px" width="172" height="172" viewBox="0 0 172 172">
    <circle cx="86" cy="86" r="84" fill="#fff" filter="drop-shadow(0 2px 4px rgba(0,0,0,.12))"/>
    <circle cx="86" cy="86" r="72" fill="none" stroke="#e2e6ec" stroke-width="5"/>
    <circle cx="86" cy="86" r="72" fill="none" stroke="#1c4a9b" stroke-width="5" stroke-dasharray="330.2 452.4" transform="rotate(-90 86 86) scale(1 -1) translate(0 -172)" stroke-linecap="round"/>
  </svg>
  <div class="abs center" style="left:316px;top:120px;width:172px"><div class="big-num" style="font-size:30px;font-weight:600">73%</div><div class="label" style="font-size:7px;margin-top:2px;font-weight:500">Project 02</div></div>
  <div class="pnum">15</div>
</section>

<section class="slide right grey" style="top:2387px">
  <h2 class="heading">Our Team</h2>
  <div class="card" style="left:48px;top:98px;width:128px;height:158px;border-radius:6px"></div>
  <div class="card" style="left:208px;top:98px;width:128px;height:158px;border-radius:6px"></div>
  <div class="card" style="left:370px;top:98px;width:128px;height:158px;border-radius:6px"></div>
  <div class="photo avatar" role="img" aria-label="Team member portrait" style="left:82px;top:118px;width:60px;height:60px"></div>
  <div class="photo avatar" role="img" aria-label="Team member portrait" style="left:242px;top:118px;width:60px;height:60px"></div>
  <div class="photo avatar" role="img" aria-label="Team member portrait" style="left:404px;top:118px;width:60px;height:60px"></div>
  <div class="plus" style="left:128px;top:112px">+</div>
  <div class="plus" style="left:288px;top:112px">+</div>
  <div class="plus" style="left:450px;top:112px">+</div>
  <div class="abs center" style="left:56px;top:184px;width:112px"><div class="label" style="font-size:6.5px">Name 01</div><p class="body center" style="margin-top:10px">Lorem ipsum dolor sit amet, consectetur adipiscing elit, sed labore et dolore magna aliqua.</p></div>
  <div class="abs center" style="left:216px;top:184px;width:112px"><div class="label" style="font-size:6.5px">Name 02</div><p class="body center" style="margin-top:10px">Lorem ipsum dolor sit amet, consectetur adipiscing elit, sed labore et dolore magna aliqua.</p></div>
  <div class="abs center" style="left:378px;top:184px;width:112px"><div class="label" style="font-size:6.5px">Name 03</div><p class="body center" style="margin-top:10px">Lorem ipsum dolor sit amet, consectetur adipiscing elit, sed labore et dolore magna aliqua.</p></div>
  <div class="pnum">16</div>
</section>

<!-- Row 9 -->
<section class="slide left" style="top:2724px">
  <div class="abs" style="left:72px;top:80px;width:200px;height:152px">
    <div class="bar-track" style="left:0;top:0;width:5px;height:140px"><div class="bar-fill" style="width:5px;height:55px;top:85px"></div></div>
    <div class="bar-track" style="left:28px;top:0;width:5px;height:140px"><div class="bar-fill" style="width:5px;height:62px;top:78px"></div></div>
    <div class="bar-track" style="left:56px;top:0;width:5px;height:140px"><div class="bar-fill" style="width:5px;height:72px;top:68px"></div></div>
    <div class="bar-track" style="left:84px;top:0;width:5px;height:140px"><div class="bar-fill" style="width:5px;height:48px;top:92px"></div></div>
    <div class="bar-track" style="left:112px;top:0;width:5px;height:140px"><div class="bar-fill" style="width:5px;height:30px;top:110px"></div></div>
    <div class="bar-track" style="left:140px;top:0;width:5px;height:140px"><div class="bar-fill" style="width:5px;height:14px;top:126px"></div></div>
    <div class="bar-track" style="left:168px;top:0;width:5px;height:140px"><div class="bar-fill" style="width:5px;height:8px;top:132px"></div></div>
  </div>
  <div class="abs" style="left:64px;top:224px;font-size:6px;color:var(--ink);word-spacing:13px;white-space:nowrap">Mon Tue Wed Thu Fri Sat Sun</div>
  <h3 class="abs title" style="left:304px;top:100px">Bar Chart Page</h3>
  <p class="abs body" style="left:304px;top:128px;width:184px">Lorem ipsum dolor sit amet, consectetur adipiscing elit, sed do eiusmod tempor incididunt ut labore et dolore magna aliqua. Ut enim ad minim veniam, quis nostrud reprehenderit in voluptate velit esse cillum dolore eu fugiat nulla pariatur. Excepteur sint occaecat anim id est laborum. Accusantium doloremque laudantium, totam rem aperiam, eaque.</p>
  <div class="pnum">17</div>
</section>

<section class="slide right" style="top:2724px">
  <h3 class="abs title" style="left:51px;top:76px">Portfolio</h3>
  <div class="abs label" style="left:51px;top:110px;font-size:6px">Client<div style="color:var(--muted);font-weight:400;font-family:'Open Sans',sans-serif">Name</div></div>
  <div class="abs label" style="left:127px;top:110px;font-size:6px">Date<div style="color:var(--muted);font-weight:400;font-family:'Open Sans',sans-serif">20 May 2020</div></div>
  <div class="abs label" style="left:203px;top:110px;font-size:6px">Category<div style="color:var(--muted);font-weight:400;font-family:'Open Sans',sans-serif">Funding</div></div>
  <p class="abs body" style="left:51px;top:138px;width:200px">Lorem ipsum dolor sit amet, consectetur adipiscing elit, sed do eiusmod tempor incididunt ut labore et dolore magna aliqua. Ut enim ad minim veniam, quis nostrud reprehenderit in voluptate velit esse cillum dolore eu fugiat nulla pariatur. Excepteur sint occaecat anim id est laborum. Accusantium doloremque laudantium, totam rem aperiam, eaque ipsa.</p>
  <div class="abs" style="left:51px;top:218px;display:flex;gap:4px"><i style="width:7px;height:7px;border:1px solid #c6ccd6;border-radius:1px"></i><i style="width:7px;height:7px;border:1px solid #c6ccd6;border-radius:1px"></i><i style="width:7px;height:7px;border:1px solid #c6ccd6;border-radius:1px"></i><i style="width:7px;height:7px;border:1px solid #c6ccd6;border-radius:1px"></i><i style="width:7px;height:7px;border:1px solid #c6ccd6;border-radius:1px"></i></div>
  <div class="photo tower" role="img" aria-label="Black and white skyscrapers against a cloudy sky" style="left:300px;top:0;width:262px;height:317px"></div>
  <div class="abs brand" style="left:474px;top:290px;color:#fff;font-size:5px"><span class="dot" style="width:5px;height:5px;margin-right:3px"></span>CORVANE CAPITAL</div>
</section>

<!-- Row 10 -->
<section class="slide left" style="top:3061px">
  <h2 class="heading">Event Page</h2>
  <div class="photo office round" role="img" aria-label="Laptop with charts on a desk" style="left:46px;top:82px;width:208px;height:96px"></div>
  <div class="photo desk round" role="img" aria-label="Team working over documents and a laptop" style="left:296px;top:82px;width:208px;height:96px"></div>
  <div class="abs label dark" style="left:52px;top:194px;font-size:9px;line-height:1">11<div style="font-size:6px">MAY</div></div>
  <div class="abs" style="left:86px;top:194px;width:170px"><div class="label" style="font-size:7.5px">Title text about Event</div><p class="body" style="margin-top:6px">Lorem ipsum dolor sit amet, adipiscing elit, sed do eiusmod tempor incididunt ut labore et dolore magna aliqua. Ut enim ad minim veniam, quis nostrud reprehenderit in voluptate velit esse</p></div>
  <div class="abs label dark" style="left:302px;top:194px;font-size:9px;line-height:1">22<div style="font-size:6px">JUN</div></div>
  <div class="abs" style="left:336px;top:194px;width:170px"><div class="label" style="font-size:7.5px">Title text about Event</div><p class="body" style="margin-top:6px">Lorem ipsum dolor sit amet, adipiscing elit, sed do eiusmod tempor incididunt ut labore et dolore magna aliqua. Ut enim ad minim veniam, quis nostrud reprehenderit in voluptate velit esse</p></div>
  <div class="pnum">19</div>
</section>

<section class="slide right" style="top:3061px">
  <div class="photo avatar" role="img" aria-label="Portrait of a smiling executive" style="left:70px;top:88px;width:104px;height:104px"></div>
  <div class="plus" style="left:160px;top:100px">+</div>
  <div class="abs center" style="left:52px;top:204px;width:140px"><div class="label" style="font-size:8px">NAME 01</div><div class="body center" style="margin-top:3px;font-size:6px">CEO Company Name</div></div>
  <h3 class="abs title" style="left:236px;top:104px">Title Text Name</h3>
  <p class="abs body" style="left:236px;top:132px;width:240px">Lorem ipsum dolor sit amet, consectetur adipiscing elit, sed do eiusmod tempor incididunt ut labore et dolore magna aliqua. Ut enim ad minim commodo consequat. Duis aute irure dolor in reprehenderit in voluptate velit esse cillum dolore eu fugiat nulla pariatur officia deserunt mollit anim id est laborum. Accusantium doloremque laudantium, totam rem aperiam.</p>
  <div class="abs label" style="left:236px;top:196px;width:240px;font-size:5.5px">Project Name 03<span style="float:right">90%</span></div>
  <div class="bar-track" style="left:236px;top:208px;width:240px"><div class="bar-fill" style="width:88%"></div></div>
  <div class="pnum">20</div>
</section>

<!-- Row 11 -->
<section class="slide left" style="top:3398px">
  <h2 class="heading">Testimonials Page</h2>
  <div class="photo avatar" role="img" aria-label="Client portrait" style="left:42px;top:88px;width:70px;height:70px"></div>
  <div class="plus" style="left:100px;top:92px">+</div>
  <div class="abs" style="left:136px;top:110px"><div class="label" style="font-size:7px">NAME 02</div><div class="body" style="margin-top:3px;font-size:6px">Company Name</div></div>
  <div class="photo avatar" role="img" aria-label="Client portrait" style="left:294px;top:88px;width:70px;height:70px"></div>
  <div class="plus" style="left:352px;top:92px">+</div>
  <div class="abs" style="left:388px;top:110px"><div class="label" style="font-size:7px">NAME 03</div><div class="body" style="margin-top:3px;font-size:6px">Company Name</div></div>
  <div class="abs" style="left:42px;top:180px;width:212px;height:72px;border-radius:8px;background:#ececec"></div>
  <div class="abs" style="left:294px;top:180px;width:212px;height:72px;border-radius:8px;background:#ececec"></div>
  <p class="abs body" style="left:58px;top:196px;width:180px;font-style:italic">Lorem ipsum dolor sit amet, adipiscing elit, sed do eiusmod tempor incididunt ut labore et dolore magna aliqua. Ut enim ad minim veniam, quis nostrud reprehenderit in voluptate velit esse</p>
  <p class="abs body" style="left:310px;top:196px;width:180px;font-style:italic">Lorem ipsum dolor sit amet, adipiscing elit, sed do eiusmod tempor incididunt ut labore et dolore magna aliqua. Ut enim ad minim veniam, quis nostrud reprehenderit in voluptate velit esse</p>
  <div class="pnum">21</div>
</section>

<section class="slide right blue" style="top:3398px">
  <h3 class="abs title" style="left:51px;top:88px;color:#fff">Contact Us</h3>
  <div class="abs" style="left:51px;top:124px;color:#fff;font-size:6px;line-height:1.4"><div style="font-size:7px">◦</div><b style="font-weight:600">Web Site</b><br>www.web.com</div>
  <div class="abs" style="left:127px;top:124px;color:#fff;font-size:6px;line-height:1.4"><div style="font-size:7px">◦</div><b style="font-weight:600">Phone Number</b><br>+ 123456789</div>
  <div class="abs" style="left:203px;top:124px;color:#fff;font-size:6px;line-height:1.4"><div style="font-size:7px">◦</div><b style="font-weight:600">Email</b><br>your@email.com</div>
  <p class="abs body" style="left:51px;top:166px;width:200px;color:#fff">Lorem ipsum dolor sit amet, consectetur adipiscing elit, sed do eiusmod tempor incididunt ut labore et dolore magna aliqua. Ut enim ad minim veniam, quis nostrud reprehenderit doloremque laudantium, totam rem aperiam, eaque ipsa.</p>
  <div class="photo arch" role="img" aria-label="Bright white modern architecture photo" style="left:330px;top:0;width:232px;height:317px"></div>
</section>

</body>
</html>
```